Tallowbrook Fitness - Personal & Rehab Training

Business Card for my personal training business - Tallowbrook Fitness. I focus on personal and rehab training. I would like a double sided card, round edges. front of card will be my existing logo and the back will have an image (black and white or exercise, people exercising, weights, etc) along with my name and details. Such as:
Corisse Pembly
Personal & Rehab Trainer
www.tallowbrookfitness.com.au
0438264905
I have some images that I have downloaded that I am happy to send to the designer.
Thanks
Target Market(s)
athletes, middle to high income, sport related
Contact Information for Business Card
Corisse Pembly
Personal & Rehab Trainer
0438264905
Colors
Designer to choose only greyscale colors for use in the design.
Requirements
Must have
- my existing logo
Nice to have
- one of the images uploaded. I really like the girl with the mint coloured shoes as this is one of my logo colours

```html
<!DOCTYPE html>
<html lang="en">
<head>
<meta charset="utf-8">
<title>Tallowbrook Fitness – Business Card</title>
<link href="https://fonts.googleapis.com/css2?family=Work+Sans:wght@400;500;700&display=swap" rel="stylesheet">
<style>
  :root {
    --backdrop: #9a9a9a;
    --card-white: #ffffff;
    --ink: #111111;
    --ink-soft: #333333;
    --rule: #1a1a1a;
    --photo-dark: #1c1c1e;
    --photo-mid: #3a3a3c;
    --photo-warm: #6b5a50;
    --mint: #9fe0b8;
    --on-dark: #ffffff;
  }
  * { margin: 0; padding: 0; box-sizing: border-box; }
  html, body {
    width: 1200px;
    height: 930px;
    overflow: hidden;
    background: var(--backdrop);
    font-family: "Work Sans", Arial, sans-serif;
  }
  .canvas { position: relative; width: 1200px; height: 930px; }

  .card {
    position: absolute;
    width: 560px;
    height: 320px;
    border-radius: 22px;
    overflow: hidden;
    box-shadow: 0 10px 24px rgba(0,0,0,0.25);
  }

  /* Front */
  .card-front { left: 50px; top: 120px; background: var(--photo-dark); }
  .front-photo {
    position: absolute; inset: 0;
    background:
      radial-gradient(ellipse at 55% 45%, var(--photo-warm) 0%, rgba(107,90,80,0) 45%),
      linear-gradient(160deg, var(--photo-mid) 0%, var(--photo-dark) 70%);
  }
  .front-brand {
    position: absolute; left: 60px; top: 130px;
    display: flex; align-items: center; gap: 18px;
  }
  .brand-square {
    width: 62px; height: 62px;
    border: 3px solid var(--mint);
    border-radius: 6px;
  }
  .brand-name-dark {
    color: var(--on-dark);
    font-weight: 500;
    font-size: 24px;
    letter-spacing: 5px;
    text-transform: uppercase;
    padding-bottom: 8px;
    border-bottom: 1.5px solid var(--on-dark);
  }

  /* Back */
  .card-back { left: 590px; top: 490px; background: var(--card-white); }
  .back-brand {
    position: absolute; right: 34px; top: 36px;
    display: flex; align-items: center; gap: 12px;
  }
  .brand-square-ink {
    width: 40px; height: 40px;
    border: 2.5px solid var(--ink);
    border-radius: 5px;
  }
  .brand-name-light {
    color: var(--ink);
    font-weight: 500;
    font-size: 16px;
    letter-spacing: 3.5px;
    text-transform: uppercase;
    padding-bottom: 6px;
    border-bottom: 1.5px solid var(--ink);
  }
  .divider-top {
    position: absolute; left: 0; right: 40px; top: 132px;
    border-top: 1px solid var(--rule);
  }
  .person { position: absolute; left: 34px; top: 172px; }
  .person-name { font-size: 26px; font-weight: 700; color: var(--ink); line-height: 1.1; }
  .person-role { font-size: 13px; color: var(--ink-soft); margin-top: 2px; }
  .divider-mid {
    position: absolute; left: 34px; width: 300px; top: 228px;
    border-top: 1px solid var(--rule);
  }
  .contact-list {
    position: absolute; left: 34px; top: 240px;
    list-style: none;
    font-size: 13px; color: var(--ink-soft);
  }
  .contact-list li { display: flex; align-items: center; gap: 8px; line-height: 22px; }
  .contact-list svg { width: 11px; height: 11px; flex: none; }
</style>
</head>
<body>
<div class="canvas">

  <section class="card card-front">
    <div class="front-photo" role="img" aria-label="Black and white gym photo of a woman in mint trainers lifting a kettlebell"></div>
    <div class="front-brand">
      <div class="brand-square"></div>
      <div class="brand-name-dark">Tallowbrook Fitness</div>
    </div>
  </section>

  <section class="card card-back">
    <div class="back-brand">
      <div class="brand-square-ink"></div>
      <div class="brand-name-light">Tallowbrook Fitness</div>
    </div>
    <div class="divider-top"></div>

    <div class="person">
      <h1 class="person-name">Corisse Pembly</h1>
      <p class="person-role">Personal &amp; Rehab Trainer</p>
    </div>
    <div class="divider-mid"></div>

    <ul class="contact-list">
      <li>
        <svg viewBox="0 0 24 24" aria-hidden="true"><path fill="#222" d="M6.6 10.8a15 15 0 0 0 6.6 6.6l2.2-2.2a1 1 0 0 1 1-.25 11.4 11.4 0 0 0 3.6.57 1 1 0 0 1 1 1V20a1 1 0 0 1-1 1A17 17 0 0 1 3 4a1 1 0 0 1 1-1h3.5a1 1 0 0 1 1 1c0 1.25.2 2.45.57 3.57a1 1 0 0 1-.25 1z"/></svg>
        0438264905
      </li>
      <li>
        <svg viewBox="0 0 24 24" aria-hidden="true"><rect x="2.5" y="5" width="19" height="14" rx="1.5" fill="none" stroke="#222" stroke-width="2"/><path d="M3 6l9 7 9-7" fill="none" stroke="#222" stroke-width="2"/></svg>
        info@tallowbrookfitness.com.au
      </li>
      <li>
        <svg viewBox="0 0 24 24" aria-hidden="true"><circle cx="12" cy="12" r="9.5" fill="none" stroke="#222" stroke-width="2"/><path d="M2.5 12h19M12 2.5c3 3 3 16 0 19M12 2.5c-3 3-3 16 0 19" fill="none" stroke="#222" stroke-width="1.6"/></svg>
        www.tallowbrookfitness.com.au
      </li>
    </ul>
  </section>

</div>
</body>
</html>
```